Innovative WordPress for a non-profit organization dedicated to providing healthcare to the less for

Bright Harbor Aid is a small non-profit organization. BHA's core mission is to provide free medical and dental care to the less fortunate. Aside from providing healthcare, BHA also helps build infrastructure such as orphanage, cancer centers, water wells and small homes for the homeless. As a non-profit, BHA has been sponsoring various social programs to help those in need. From building infrastructure to health care and most recently micro-finance, the BHA team is helping to GIve Back to the community at person at a time.

BHA is growing and needs help to restructure for the future. The corporate website design is the first step in a new branding strategy for the company.

BHA current website is divided into three specific target areas:
1. Mission: This area is dedicated to provide information about medical and dental mission hosted by BHA.

2. Infrastructure. This area is dedicated to provide information about infrastructure programs supported and completed by the BHA team. The projects includes orphanage, cancer centers. water wells, micro-finance, small homes for the homeless...etc.

3. Special Projects. This area is used to showcase specific short term projects which might come up.

Aside from the specific three target area, BHA also needs a NEWS area where news about BHA can be published.

Please put your thinking cape on and help produce the next generation WordPress template for Bright Harbor Aid. Your design will great enhance the level of volunteers recruited and also increase the level of help that BHA can provide for other.

For a quick glance at the BHA website today, please visit http://www.bhaexample.org. The BHA team is looking for a fresh design.

Thank you very much for taking the time to help BHA advance its mission of helping those in need.

Reason: Seeking more variety in design. Design needs to have a donate button, sponsors area, news, welcome message, 3 primary functions (mission, infrastructure, and specials projects). The BHA logo is available. Please note, you have the option to NOT use the colors associated with BHA logo. Thank you for helping with designing the new site.

Non-Profit

Requirements
Must have
• 1. Donate Now button.
2. Primary focus areas: MISSION / INFRASTRUCTURE / SPECIAL PROJECTS
3. News & Events
4. Welcome Message area
5. Sponsors area - place to add sponsor logos

Nice to have
• 1. Photo of the Month: Used to show a specific photo to represent events or functions completed by the BHA team.

Please show sample of one level down. For example, what does the page look like when I click the MISSION link.

```html
<!DOCTYPE html>
<html lang="en">
<head>
<meta charset="utf-8">
<title>Bright Harbor Aid</title>
<link href="https://fonts.googleapis.com/css2?family=Open+Sans:wght@400;600;700&display=swap" rel="stylesheet">
<style>
:root{
  --green:#2f9a3c;
  --green-dark:#237a2e;
  --ink:#333;
  --muted:#777;
  --line:#e2e2e2;
  --footer:#e6e6e6;
  --footer-dark:#d2d2d2;
  --photo-a:#8a6f55;
  --photo-b:#c8b49a;
}
*{box-sizing:border-box;margin:0;padding:0}
html,body{width:837px;height:1200px;overflow:hidden;background:#fff}
body{font-family:"Open Sans",sans-serif;color:var(--ink);font-size:7px;line-height:1.45;position:relative}
.header{height:46px;display:flex;align-items:center;justify-content:space-between;padding:0 56px}
.brand{display:flex;align-items:center;gap:6px;font-weight:700;font-size:20px;color:var(--green)}
.brand-dot{width:16px;height:16px;border-radius:50%;background:var(--green)}
.header-tools{display:flex;flex-direction:column;align-items:flex-end;gap:5px}
.socials{display:flex;gap:4px}
.socials span{width:10px;height:10px;background:#bbb;border-radius:2px}
.donate{background:var(--green);color:#fff;font-weight:700;font-size:8px;padding:4px 14px;border-radius:3px}
.nav{height:20px;background:var(--green);display:flex;align-items:center;gap:22px;padding:0 56px;color:#fff;font-size:7px;font-weight:600}
.hero{height:200px;position:relative;overflow:hidden;
  background:
    radial-gradient(ellipse 180px 140px at 170px 120px,rgba(240,228,205,.55),transparent 70%),
    radial-gradient(ellipse 160px 150px at 700px 140px,rgba(60,110,60,.35),transparent 70%),
    linear-gradient(180deg,rgba(255,255,255,.15),rgba(0,0,0,.25)),
    linear-gradient(100deg,#6e5640,#a88a68 30%,#cbb898 55%,#9c8266 80%,#5f4a37)}
.hero-caption{position:absolute;left:412px;top:68px;width:340px;padding:8px 12px;background:rgba(20,60,25,.72);color:#fff;font-weight:700;font-size:14px;line-height:1.25}
.hero-caption small{display:block;font-size:6.5px;font-weight:400;margin-top:4px;line-height:1.4}
.hero-dots{position:absolute;right:56px;bottom:10px;display:flex;gap:4px}
.hero-dots span{width:6px;height:6px;border-radius:50%;background:rgba(255,255,255,.6)}
.hero-dots span:first-child{background:var(--green)}
.pillars{display:flex;justify-content:space-between;padding:0 96px;margin-top:12px}
.pillar{width:190px;text-align:center}
.pillar-icon{width:58px;height:58px;border-radius:50%;margin:0 auto;border:3px solid var(--green);background:linear-gradient(135deg,var(--photo-a),var(--photo-b))}
.pillar h3{font-size:8.5px;font-weight:700;margin:8px 0 5px;letter-spacing:.3px}
.pillar p{color:var(--muted);font-size:6.5px;height:42px}
.btn{display:inline-block;background:var(--green);color:#fff;font-size:6.5px;font-weight:600;padding:3px 14px;border-radius:2px}
.divider{margin:22px 56px 0;border-top:1px solid var(--line)}
.main{display:flex;gap:16px;padding:14px 56px 0}
.content{width:572px}
.sidebar{width:137px}
h2{font-size:14px;font-weight:600;color:#444;margin-bottom:6px}
.welcome p{font-size:6.5px;color:#555;margin-bottom:6px}
.section-head{display:flex;justify-content:space-between;align-items:center;margin-top:14px}
.arrows{display:flex;gap:3px}
.arrows span{width:10px;height:10px;background:var(--green)}
.photos{display:flex;gap:10px;margin-top:4px}
.photo{width:135px}
.photo-img{height:90px;background:linear-gradient(135deg,var(--photo-a),var(--photo-b))}
.photo p{font-size:6px;color:var(--muted);margin-top:3px}
.dots{display:flex;justify-content:center;gap:4px;margin-top:6px}
.dots span{width:5px;height:5px;border-radius:50%;background:#ccc}
.dots span:first-child{background:var(--green)}
.sponsors{display:flex;gap:34px;align-items:center;margin-top:16px;padding-left:10px}
.badge{width:90px;height:58px;background:#dfe7e0;border-radius:4px}
.badge.round{width:58px;border-radius:50%}
.side-title{background:var(--green);color:#fff;font-weight:700;font-size:8px;padding:4px 7px}
.news-item{display:flex;gap:5px;padding:6px 0;border-bottom:1px solid var(--line)}
.news-thumb{width:26px;height:24px;flex:none;background:linear-gradient(135deg,var(--photo-a),var(--photo-b))}
.news-item b{display:block;font-size:6.5px;color:var(--green)}
.news-item span{font-size:6px;color:var(--muted)}
.map{height:150px;background:linear-gradient(135deg,#e8e4d8,#cfd9c4);margin-top:6px}
.footer{position:absolute;left:0;top:982px;width:837px;height:176px;background:var(--footer);display:flex;gap:30px;padding:16px 56px}
.footer h4{font-size:9px;font-weight:700;margin-bottom:6px;color:#444}
.footer p{font-size:6.5px;color:#666}
.about{width:410px}
.connect{display:flex;gap:30px;margin-top:6px}
.connect div{display:flex;align-items:center;gap:4px;font-size:6px;color:#666}
.connect i{width:14px;height:14px;border-radius:50%;background:var(--green);display:block}
.offers{width:230px}
.field{height:14px;background:#fff;border:1px solid #ccc;margin:6px 0 4px}
.bottom-bar{position:absolute;left:0;top:1158px;width:837px;height:42px;background:var(--footer-dark);display:flex;justify-content:space-between;align-items:center;padding:0 56px;font-size:6px;color:#666}
.bottom-bar nav{display:flex;gap:12px}
</style>
</head>
<body>
<header class="header">
  <div class="brand"><span class="brand-dot"></span>BHA</div>
  <div class="header-tools">
    <div class="socials"><span></span><span></span><span></span></div>
    <div class="donate">Donate Now</div>
  </div>
</header>
<nav class="nav"><span>Home</span><span>About Us</span><span>Mission</span><span>Infrastructure</span><span>Special Projects</span><span>News</span><span>Contact</span></nav>
<section class="hero" role="img" aria-label="Photo of volunteer doctors at a free dental clinic">
  <div class="hero-caption">Dr. Lena Marsh and Dr. Owen Hale at a BHA hosted free Dental Clinic.
    <small>Volunteers served more than two hundred patients during the weekend clinic.</small></div>
  <div class="hero-dots"><span></span><span></span><span></span></div>
</section>
<section class="pillars">
  <div class="pillar"><div class="pillar-icon" role="img" aria-label="Infrastructure project photo"></div><h3>INFRASTRUCTURE</h3><p>We help build orphanages, cancer centers, water wells and small homes so families gain a safe and lasting place to live and heal.</p><span class="btn">Read More</span></div>
  <div class="pillar"><div class="pillar-icon" role="img" aria-label="Medical mission photo"></div><h3>MISSION</h3><p>Through our free medical and dental missions, volunteer doctors bring care to communities that have little or no access to it.</p><span class="btn">Read More</span></div>
  <div class="pillar"><div class="pillar-icon" role="img" aria-label="Special project photo"></div><h3>SPECIAL PROJECTS</h3><p>Short term projects respond to urgent needs as they arise, from relief supplies to micro-finance for small family businesses.</p><span class="btn">Read More</span></div>
</section>
<div class="divider"></div>
<main class="main">
  <div class="content">
    <section class="welcome">
      <h2>Welcome Message area</h2>
      <p>Bright Harbor Aid is a small non-profit dedicated to providing free medical and dental care to the less fortunate. Our volunteers travel to towns and villages where care is scarce, working side by side with local partners to treat patients and teach healthy habits that last long after each mission ends.</p>
      <p>Beyond healthcare, we build lasting infrastructure and support programs that help families stand on their own. Orphanages, cancer centers, water wells and small homes for the homeless have all grown from the generosity of people who believe that good health and a safe home belong to everyone.</p>
      <p>Every gift and every volunteer hour helps us give back to the community one person at a time. Whether you can lend your skills on a mission, sponsor a project or share our story with friends, there is a place for you on our team. Join us and help shape the next chapter of our work.</p>
    </section>
    <div class="section-head"><h2>Photo of the Month</h2><div class="arrows"><span></span><span></span></div></div>
    <div class="photos">
      <div class="photo"><div class="photo-img" role="img" aria-label="Event photo"></div><p>Clinic day</p></div>
      <div class="photo"><div class="photo-img" role="img" aria-label="Event photo"></div><p>New well</p></div>
      <div class="photo"><div class="photo-img" role="img" aria-label="Event photo"></div><p>Volunteers</p></div>
      <div class="photo"><div class="photo-img" role="img" aria-label="Event photo"></div><p>Home build</p></div>
    </div>
    <div class="dots"><span></span><span></span><span></span></div>
    <h2 style="margin-top:10px">Sponsors Area</h2>
    <div class="sponsors">
      <div class="badge round"></div><div class="badge round"></div><div class="badge"></div><div class="badge round"></div><div class="badge"></div>
    </div>
  </div>
  <aside class="sidebar">
    <div class="side-title">News &amp; Events</div>
    <div class="news-item"><div class="news-thumb" role="img" aria-label="News photo"></div><div><b>New clinic opens soon</b><span>Read more details here</span></div></div>
    <div class="news-item"><div class="news-thumb" role="img" aria-label="News photo"></div><div><b>Water well completed</b><span>Read more details here</span></div></div>
    <div class="news-item"><div class="news-thumb" role="img" aria-label="News photo"></div><div><b>Volunteers needed now</b><span>Read more details here</span></div></div>
    <div class="news-item"><div class="news-thumb" role="img" aria-label="News photo"></div><div><b>Spring dental mission</b><span>Read more details here</span></div></div>
    <div class="news-item"><div class="news-thumb" role="img" aria-label="News photo"></div><div><b>Micro-finance update</b><span>Read more details here</span></div></div>
    <div class="news-item"><div class="news-thumb" role="img" aria-label="News photo"></div><div><b>Annual report posted</b><span>Read more details here</span></div></div>
    <div class="side-title" style="margin-top:10px">Our Location</div>
    <div class="map" role="img" aria-label="Map of office location"></div>
  </aside>
</main>
<footer class="footer">
  <div class="about">
    <h4>About Us</h4>
    <p>Bright Harbor Aid brings free medical and dental care to people in need and builds the homes, wells and centers that keep communities strong. We rely on volunteers and donors who share our belief that good health is a right for everyone.</p>
    <h4 style="margin-top:12px">Connect With Us</h4>
    <div class="connect"><div><i></i>Follow us</div><div><i></i>Follow us</div><div><i></i>Watch us</div></div>
  </div>
  <div class="offers">
    <h4>Get Our Special Offers</h4>
    <p>Subscribe to hear about new missions and events.</p>
    <div class="field"></div>
    <span class="btn">Subscribe Now</span>
  </div>
</footer>
<div class="bottom-bar"><span>Copyright © Bright Harbor Aid · http://www.bhaexample.org</span><nav><span>Home</span><span>About Us</span><span>Mission</span><span>Projects</span><span>Contact</span></nav></div>
</body>
</html>
```